sydney wedding photography business needs a business card design

we need a business card design for a sydney based wedding photography and videography business. our business name is :golden hour photography and video. our target clients are 24-35 yrs female. our style is candid, organic, natural, dynamic. we are a team of young photographers and videographers, and help brides to create memories that they will cherish for the rest of their lives. the logo will be provided. we want an elegant design that reflects our style, and also want to give a great impression to our clients that we are one of the best studios in sydney and our brand means quality and premium service.

Target Market(s)

bride to be, 24-35 years old, living in sydney and surrunding areas

Industry/Entity Type

Wedding Photography

Contact Information for Business Card

address: 57 marrow lane, bexton nsw 2041
mobile: 0431872056
phone: (02) 9361 2748
info@goldenhourstudio.net.au
www.goldenhourstudio.net.au
facebook:goldenhourbridals
instagram:goldenhourbridals

Font styles to use
Serif
Sans Serif

Requirements
Nice to have
• maybe add my slogan"memories beyond eternity" if the layout looks good
Should not have
• no black color, not good idea for wedding biz card

```html
<!DOCTYPE html>
<html lang="en">
<head>
<meta charset="utf-8">
<title>Golden Hour – Business Card</title>
<link href="https://fonts.googleapis.com/css2?family=Lora:ital,wght@0,400;0,600;1,400&family=Montserrat:wght@400&display=swap" rel="stylesheet">
<style>
  :root {
    --bg: #e9e4dc;
    --band: #6b5849;
    --band-deep: #5c4a3d;
    --paper: #faf7f2;
    --gold-dark: #c48f1a;
    --gold-light: #f3d572;
    --gold-text: #e0b247;
    --gold-ink: #b8862a;
    --grey-text: #6a625c;
  }
  * { margin: 0; padding: 0; box-sizing: border-box; }
  html, body { width: 1200px; height: 864px; overflow: hidden; background: var(--bg); }
  .canvas {
    width: 1200px; height: 864px;
    display: flex; align-items: center; justify-content: center; gap: 60px;
  }
  .card {
    position: relative;
    width: 525px; height: 300px;
    box-shadow: 0 10px 30px rgba(60,40,20,.18);
    overflow: hidden;
  }
  .card-back {
    background: linear-gradient(135deg, var(--band), var(--band-deep));
    display: flex; flex-direction: column; align-items: center; justify-content: center; gap: 10px;
  }
  .brand {
    display: flex; align-items: center; gap: 14px;
    font-family: "Lora", serif; font-weight: 600; color: var(--gold-text);
  }
  .brand-dot { width: 12px; height: 12px; border-radius: 50%; background: var(--gold-text); }
  .card-back .brand { font-size: 46px; }
  .subline {
    font-family: "Montserrat", sans-serif; font-size: 13px; letter-spacing: .45em;
    color: var(--gold-text); text-transform: uppercase; padding-left: .45em;
  }
  .card-front { background: var(--paper); }
  .front-art { position: absolute; inset: 0; }
  .front-brand { position: absolute; top: 22px; right: 34px; display: flex; flex-direction: column; align-items: flex-end; gap: 4px; }
  .front-brand .brand { font-size: 30px; }
  .front-brand .subline { font-size: 9px; }
  .person { position: absolute; left: 32px; top: 148px; font-family: "Lora", serif; }
  .person-name { font-size: 25px; color: var(--grey-text); }
  .person-role { font-size: 14px; font-style: italic; color: var(--gold-ink); margin-top: 2px; }
  .contacts {
    position: absolute; right: 28px; bottom: 18px; width: 262px;
    list-style: none; font-family: "Lora", serif; font-size: 12px; color: var(--grey-text);
  }
  .contacts li { display: flex; align-items: center; gap: 8px; line-height: 1.58; white-space: nowrap; }
  .contacts svg { width: 11px; height: 11px; flex: none; }
</style>
</head>
<body>
<main class="canvas">
  <section class="card card-back" aria-label="Card back">
    <div class="brand"><span class="brand-dot"></span>Golden Hour</div>
    <p class="subline">Photography &amp; Video</p>
  </section>

  <section class="card card-front" aria-label="Card front">
    <svg class="front-art" viewBox="0 0 525 300" preserveAspectRatio="none" aria-hidden="true">
      <defs>
        <linearGradient id="goldLine" x1="0" y1="0" x2="1" y2="0">
          <stop offset="0" stop-color="#c48f1a"/>
          <stop offset=".5" stop-color="#f3d572"/>
          <stop offset="1" stop-color="#c48f1a"/>
        </linearGradient>
        <linearGradient id="bandFill" x1="0" y1="0" x2="1" y2="1">
          <stop offset="0" stop-color="#6b5849"/>
          <stop offset="1" stop-color="#5c4a3d"/>
        </linearGradient>
      </defs>
      <path d="M0 0 H525 V128 C380 124 170 116 0 98 Z" fill="url(#bandFill)"/>
      <path d="M0 98 C170 116 380 124 525 128" fill="none" stroke="url(#goldLine)" stroke-width="5"/>
    </svg>

    <div class="front-brand">
      <div class="brand"><span class="brand-dot"></span>Golden Hour</div>
      <p class="subline">Photography &amp; Video</p>
    </div>

    <div class="person">
      <p class="person-name">Ella Hart</p>
      <p class="person-role">Photography</p>
    </div>

    <ul class="contacts">
      <li>
        <svg viewBox="0 0 12 12"><rect x="3" y="1" width="6" height="10" rx="1" fill="none" stroke="var(--gold-ink)" stroke-width="1.2"/></svg>
        0431 872 056
      </li>
      <li>
        <svg viewBox="0 0 12 12"><path d="M2.5 1.5 L4.5 1.5 L5.5 4 L4 5 C4.8 6.7 5.3 7.2 7 8 L8 6.5 L10.5 7.5 L10.5 9.5 C6 10 2 6 2.5 1.5 Z" fill="var(--gold-ink)"/></svg>
        (02) 9361 2748
      </li>
      <li>
        <svg viewBox="0 0 12 12"><rect x="1" y="2.5" width="10" height="7" fill="var(--gold-ink)"/><path d="M1 2.5 L6 7 L11 2.5" fill="none" stroke="var(--paper)" stroke-width="1"/></svg>
        info@goldenhourstudio.net.au
      </li>
      <li>
        <svg viewBox="0 0 12 12"><circle cx="6" cy="6" r="5" fill="var(--gold-ink)"/><path d="M1 6 H11 M6 1 V11" stroke="var(--paper)" stroke-width=".8"/></svg>
        www.goldenhourstudio.net.au
      </li>
      <li>
        <svg viewBox="0 0 12 12"><path d="M6 11 C3 7.5 2 6 2 4.5 A4 4 0 0 1 10 4.5 C10 6 9 7.5 6 11 Z" fill="var(--gold-ink)"/><circle cx="6" cy="4.5" r="1.4" fill="var(--paper)"/></svg>
        57 Marrow Lane, Bexton NSW 2041
      </li>
      <li>
        <svg viewBox="0 0 12 12"><circle cx="6" cy="6" r="4.5" fill="none" stroke="var(--gold-ink)" stroke-width="1.2"/></svg>
        facebook &amp; instagram: goldenhourbridals
      </li>
    </ul>
  </section>
</main>
</body>
</html>
```